Birchfield Dental Care Stationery

create stationery, business cards and envelops for business. Use current logo on website but open to new fonts for the business name. Business name is Birchfield Dental Care, would like below the name added "Cosmetic - Family - Implants" Website is www.birchfielddentalcareQX.example. I would like to have modern look, clean, and professional. The water mark of the logo is a great thing to ad as well.

Target Market(s)

General public, Families, Cosmetic, Implant

Industry/Entity Type

Dental

Font styles to use
Sans Serif

Colors
9bcb3c
000000
757575
c9c9c9

Requirements
Must have
• Would like to see different versions of the current logo. Improvements, color, sytle, and class.
Nice to have
• current font has double "oo" in the Birchfield logo, does not need to have with new logo.

```html
<!DOCTYPE html>
<html lang="en">
<head>
<meta charset="utf-8">
<title>Birchfield Dental Care – Business Card</title>
<link rel="stylesheet" href="https://fonts.googleapis.com/css2?family=Open+Sans:wght@400;600;700&display=swap">
<style>
  :root {
    --page: #e4e4e4;
    --slate: #2f3744;
    --lime: #95c83e;
    --white: #ffffff;
    --ink: #333a45;
    --grey: #757575;
  }
  html, body {
    margin: 0;
    padding: 0;
    width: 1200px;
    height: 987px;
    overflow: hidden;
    background: var(--page);
    font-family: "Open Sans", Arial, sans-serif;
  }
  .card {
    position: absolute;
    left: 293px;
    width: 615px;
    height: 351px;
    border-radius: 18px;
    overflow: hidden;
  }
  .card--front { top: 130px; background: var(--white); }
  .card--back { top: 506px; background: var(--lime); }

  .front-art { position: absolute; inset: 0; width: 100%; height: 100%; }

  .identity {
    position: absolute;
    left: 67px;
    top: 177px;
    width: 260px;
    transform: translate(-50%, -50%) rotate(-90deg);
    color: var(--white);
    line-height: 1.2;
  }
  .identity__name {
    margin: 0 0 2px;
    font-size: 20px;
    font-weight: 700;
    color: var(--lime);
  }
  .identity__role {
    margin: 0;
    font-size: 15px;
    font-weight: 400;
  }

  .brand {
    position: absolute;
    display: flex;
    align-items: center;
  }
  .brand__ring {
    flex: none;
    border-radius: 50%;
    box-sizing: border-box;
  }
  .brand__name {
    margin: 0;
    font-weight: 700;
    text-transform: uppercase;
    line-height: 1.02;
    letter-spacing: 0.5px;
  }
  .brand__tagline {
    margin: 3px 0 0;
    font-weight: 700;
    text-transform: uppercase;
    letter-spacing: 0.6px;
  }

  .brand--front { left: 264px; top: 70px; }
  .brand--front .brand__ring { width: 60px; height: 60px; border: 4px solid var(--lime); margin-right: 10px; }
  .brand--front .brand__name { font-size: 22px; color: var(--ink); }
  .brand--front .brand__tagline { font-size: 9.5px; color: var(--grey); }

  .contact {
    position: absolute;
    left: 387px;
    top: 154px;
    transform: translateX(-50%);
    text-align: center;
    color: var(--ink);
    font-size: 15px;
    line-height: 23px;
    white-space: nowrap;
  }
  .contact p { margin: 0; }
  .contact__address { margin-bottom: 6px !important; }
  .contact__label { color: var(--lime); font-weight: 600; }

  .brand--back { left: 50%; top: 50%; transform: translate(-50%, -50%); }
  .brand--back .brand__ring { width: 94px; height: 94px; border: 6px solid var(--white); margin-right: 14px; }
  .brand--back .brand__name { font-size: 35px; color: var(--white); }
  .brand--back .brand__tagline { font-size: 13px; color: var(--white); }
</style>
</head>
<body>
  <section class="card card--front">
    <svg class="front-art" viewBox="0 0 525 299" preserveAspectRatio="none" aria-hidden="true">
      <rect width="525" height="299" fill="var(--slate)"/>
      <circle cx="298" cy="150" r="190" fill="var(--lime)"/>
      <circle cx="310" cy="150" r="186" fill="var(--white)"/>
      <rect x="330" y="0" width="195" height="299" fill="var(--white)"/>
    </svg>

    <div class="identity">
      <p class="identity__name">Dr. Nathan Ferrell D.D.S.</p>
      <p class="identity__role">Maple Grove Cosmetic,</p>
      <p class="identity__role">Family, &amp; Sedation Dentist</p>
    </div>

    <div class="brand brand--front">
      <span class="brand__ring"></span>
      <div>
        <p class="brand__name">Birchfield<br>Dental Care</p>
        <p class="brand__tagline">Cosmetic - Family - Implants</p>
      </div>
    </div>

    <div class="contact">
      <p>1840 Larkspur Ave</p>
      <p class="contact__address">Maple Grove, QX 10482-3310</p>
      <p><span class="contact__label">Phone:</span> 555-014-2287</p>
      <p>nathan@birchfielddentalcareqx.example</p>
      <p>www.birchfielddentalcareQX.example</p>
    </div>
  </section>

  <section class="card card--back">
    <div class="brand brand--back">
      <span class="brand__ring"></span>
      <div>
        <p class="brand__name">Birchfield<br>Dental Care</p>
        <p class="brand__tagline">Cosmetic - Family - Implants</p>
      </div>
    </div>
  </section>
</body>
</html>
```